"Autumn Special" 6 Month Membership Special

Running a Membership Drive on a 6 month membership option for the month of April/May. 6 months $150.00 save 50%. Below is recent ads made from designers on Mural Nest to assist. Final design should be inviting / colorful and eye catching

Format required is for a Facebook cover, Instagram, and A0 format for a poster .

Target Market(s)

16-40 male and female

Industry/Entity Type

Fitness

Font styles to use
Serif
Other font styles liked:
• Athletic

Colors

Designer to choose colors to be used in the design.

Requirements
Must have
• The main emphasis would be on the "6 MONTH SPECIAL" or "AUTUMN SPECIAL" font/text (special) and the layout of the text. If we can add some brighter colors to the layout that would be great just to capture their attention. If there's any effects you want to add to it that would be great. The logo can be faint in the background. The image of the female model can some some artistic effects around it and she does not have to be the main focus
• "AUTUMN SPECIAL"
• 6 MONTHS from
• $150.00
• SAVE 50%"
• "Terms and conditions apply"
• All contact details, address, website, etc which will be supplied
Nice to have
• Some artistic effects to catch your eye and enhance the professionalism of the designer. Attached is a "Athletic font" Logo which that style could be incorporated
Should not have
• You don't have to include the orange background of the female model, you can use her silhouette

```html
<!DOCTYPE html>
<html lang="en">
<head>
<meta charset="utf-8">
<title>Kestrel Gymnasium – Autumn Special</title>
<link rel="stylesheet" href="https://fonts.googleapis.com/css2?family=Anton&family=Archivo+Black&family=Montserrat:wght@300;400&display=swap">
<style>
  :root{
    --sun:#fbd86c;
    --sun-deep:#f3c44a;
    --ink:#0b0b0b;
    --paper:#ffffff;
    --kit-blue:#5d7390;
    --kit-shade:#3f4f66;
  }
  *{margin:0;padding:0;box-sizing:border-box}
  html,body{width:1200px;height:1200px;overflow:hidden;background:var(--sun)}
  .poster{position:relative;width:1200px;height:1200px;overflow:hidden;
    background:radial-gradient(circle at 70% 75%, var(--sun) 0%, var(--sun-deep) 120%);}
  .brush-stripe{position:absolute;inset:0;width:1200px;height:1200px}
  .athlete-photo{position:absolute;left:40px;top:270px;width:420px;height:710px}

  .brand{position:absolute;left:92px;top:78px;width:330px;color:var(--ink);
    font-family:"Archivo Black",sans-serif;text-align:center;line-height:1}
  .brand-name{display:block;font-size:84px;letter-spacing:-1px}
  .brand-sub{display:block;font-size:27px;letter-spacing:14px;margin-top:10px;padding-left:14px}

  .headline{position:absolute;left:330px;top:190px;width:960px;text-align:center;
    font-family:"Anton",sans-serif;color:var(--sun);font-size:205px;line-height:.86;
    letter-spacing:6px;text-transform:uppercase;transform:rotate(-31deg) skewX(-6deg);
    transform-origin:center}
  .headline span{display:block}

  .tag{position:absolute;background:var(--ink);color:var(--sun);
    font-family:"Archivo Black",sans-serif;font-size:64px;line-height:76px;
    padding:0 14px;white-space:nowrap;text-align:right}
  .tag-months{left:733px;top:616px;width:417px}
  .tag-special{left:827px;top:702px;width:323px}

  .save{position:absolute;left:480px;top:780px;color:var(--ink);line-height:1}
  .save-word{display:block;font-family:"Montserrat",sans-serif;font-weight:300;font-size:100px;letter-spacing:2px}
  .save-figure{display:block;font-family:"Archivo Black",sans-serif;font-size:152px;margin-top:-4px;letter-spacing:-4px}
  .save-figure small{font-size:70px;vertical-align:top;position:relative;top:14px;letter-spacing:0}

  .divider{position:absolute;left:787px;top:782px;width:3px;height:214px;background:var(--ink)}

  .price{position:absolute;left:836px;top:800px;color:var(--ink);line-height:1}
  .price-term{display:block;font-family:"Archivo Black",sans-serif;font-size:52px}
  .price-from{display:block;font-family:"Montserrat",sans-serif;font-size:21px;margin:10px 0 0 6px}
  .price-amount{display:block;font-family:"Archivo Black",sans-serif;font-size:74px;margin-top:8px;letter-spacing:-1px}

  .website{position:absolute;left:488px;top:1030px;width:650px;text-align:center;
    font-family:"Archivo Black",sans-serif;font-size:47px;color:var(--ink);letter-spacing:-.5px}

  .contact-bar{position:absolute;left:0;top:1116px;width:1200px;height:84px;background:var(--ink);
    display:flex;align-items:center;justify-content:space-between;padding:0 20px 0 46px;
    color:var(--paper);font-family:"Montserrat",sans-serif;font-weight:400;font-size:29px}
  .contact-item{display:flex;align-items:center;gap:18px;white-space:nowrap}
  .contact-item svg{fill:var(--paper);flex:none}
</style>
</head>
<body>
<main class="poster">
  <svg class="brush-stripe" viewBox="0 0 1200 1200" aria-hidden="true">
    <polygon fill="var(--ink)" points="0,540 1168,0 1200,0 1200,330 0,1010"/>
  </svg>

  <svg class="athlete-photo" viewBox="0 0 420 710" role="img" aria-label="Photo of a female athlete in a blue-grey gym set mid-stride holding dumbbells, with falling autumn leaves">
    <defs>
      <linearGradient id="athleteTone" x1="0" y1="0" x2="1" y2="1">
        <stop offset="0" stop-color="var(--kit-blue)"/>
        <stop offset="1" stop-color="var(--kit-shade)"/>
      </linearGradient>
    </defs>
    <rect width="420" height="710" rx="40" fill="url(#athleteTone)" opacity=".9"/>
  </svg>

  <div class="brand">
    <span class="brand-name">KESTREL</span>
    <span class="brand-sub">GYMNASIUM</span>
  </div>

  <h1 class="headline"><span>Autumn</span><span>Special</span></h1>

  <div class="tag tag-months">6 MONTHS</div>
  <div class="tag tag-special">SPECIAL</div>

  <div class="save">
    <span class="save-word">SAVE</span>
    <span class="save-figure">50<small>%</small></span>
  </div>

  <div class="divider"></div>

  <div class="price">
    <span class="price-term">6 MONTHS</span>
    <span class="price-from">FROM</span>
    <span class="price-amount">$150.00</span>
  </div>

  <p class="website">www.kestrelgym.com.au</p>

  <footer class="contact-bar">
    <span class="contact-item">
      <svg width="30" height="42" viewBox="0 0 24 34"><path d="M12 0C5.4 0 0 5.3 0 11.9 0 20.6 12 34 12 34s12-13.4 12-22.1C24 5.3 18.6 0 12 0zm0 17a5.2 5.2 0 1 1 0-10.4A5.2 5.2 0 0 1 12 17z"/></svg>
      14 Larch Rd Eastfield
    </span>
    <span class="contact-item">
      <svg width="40" height="40" viewBox="0 0 24 24"><path d="M6.6 10.8a15.2 15.2 0 0 0 6.6 6.6l2.2-2.2c.3-.3.7-.4 1-.2 1.1.4 2.3.6 3.6.6.6 0 1 .4 1 1V20c0 .6-.4 1-1 1A17 17 0 0 1 3 4c0-.6.4-1 1-1h3.5c.6 0 1 .4 1 1 0 1.3.2 2.5.6 3.6.1.3 0 .7-.2 1z"/></svg>
      9481 2265
    </span>
    <span class="contact-item">
      <svg width="44" height="38" viewBox="0 0 44 38"><path d="M2 14 22 2l20 12v22H2z" fill="none" stroke="var(--paper)" stroke-width="3"/><path d="M2 14l20 13 20-13" fill="none" stroke="var(--paper)" stroke-width="3"/><text x="22" y="20" font-family="Montserrat,sans-serif" font-size="14" text-anchor="middle" fill="var(--paper)">@</text></svg>
      kestrelgym@mail.com.au
    </span>
  </footer>
</main>
</body>
</html>
```